Buch-/E-Book-Cover für Tagebuchroman
sehr auf meine Wünsche eingegangen, schnell, hilfsbereit und sehr genau
Zielgruppe
Ich bin Schriftstellerin - mein Roman richtet sich an Jugendliche (12-16 Jahre), in erster Linie Mädchen.
Ich benötige ein Cover für e-book und Paperback.
Aufgabenstellung
Es sollte ein junges, flottes Cover sein. Das Buch ist ein Tagebuchroman, dh es könnte z.B. wie das Tagebuch der 14-jährigen Protagonistin gestaltet sein. (Buchtitel ist 'Kritzeleien aus Zimmer Neun')
zum Inhalt:
Die 14-jährige Lena ist – als Gedichte schreibende Pessimistin – eindeutig anders. Dabei möchte sie so gerne „dazugehören“! Zum Glück hat Lena einen genialen Plan: Sie beschließt, von nun an positiv zu denken. Doch da ist der neue Mathelehrer, bei dem sie immer so ein eigenartiges Bauchkribbeln bekommt, ein peinliches ClipWelle-Video taucht auf und die Erzfeindin in der Schule ist gemeiner denn je. Und dann zieht auch noch eine neue Familie ins Nachbarhaus: Deren Zwillinge – die coole Jule und der nervige Torben – stellen Lenas Leben komplett auf den Kopf…
Eine turbulente Geschichte über das Anderssein, Freundschaft und die erste Liebe…

```html
<!DOCTYPE html>
<html lang="de">
<head>
<meta charset="utf-8">
<title>Kritzeleien aus Zimmer Neun – Cover</title>
<link rel="stylesheet" href="https://fonts.googleapis.com/css2?family=Mr+Dafoe&family=Saira+Condensed:wght@300;400&display=swap">
<style>
  :root {
    --backdrop: #e6e6e4;
    --cover-pink: #f5bfc6;
    --doodle-tone: #dca2ab;
    --doodle-line: #8d7a7d;
    --ink: #141213;
  }
  html, body {
    margin: 0;
    padding: 0;
    width: 1200px;
    height: 1200px;
    overflow: hidden;
    background: var(--backdrop);
  }
  .canvas {
    position: relative;
    width: 1200px;
    height: 1200px;
  }
  .cover {
    position: absolute;
    left: 208px;
    top: 40px;
    width: 785px;
    height: 1120px;
    background: var(--cover-pink);
    overflow: hidden;
  }
  .doodles {
    position: absolute;
    left: 0;
    top: 0;
    width: 785px;
    height: 1120px;
  }
  .doodle {
    fill: var(--doodle-tone);
    opacity: 0.55;
  }
  .doodle-arrow {
    fill: none;
    stroke: var(--doodle-line);
    stroke-width: 2;
    stroke-linecap: round;
  }
  .title {
    position: absolute;
    left: 0;
    top: 0;
    width: 100%;
    height: 100%;
    margin: 0;
    font-weight: normal;
  }
  .title__script {
    position: absolute;
    left: 0;
    width: 100%;
    text-align: center;
    font-family: "Mr Dafoe", cursive;
    color: var(--ink);
    line-height: 1;
  }
  .title__script--first { top: 262px; font-size: 150px; left: -10px; }
  .title__script--last { top: 518px; font-size: 190px; left: 10px; }
  .title__link {
    position: absolute;
    top: 455px;
    left: 0;
    width: 100%;
    text-align: center;
    font-family: "Saira Condensed", sans-serif;
    font-weight: 300;
    font-size: 92px;
    letter-spacing: 4px;
    color: var(--ink);
    line-height: 1;
    padding-left: 150px;
    box-sizing: border-box;
  }
  .author {
    position: absolute;
    right: 70px;
    top: 1010px;
    margin: 0;
    font-family: "Saira Condensed", sans-serif;
    font-weight: 300;
    font-size: 56px;
    letter-spacing: 8px;
    color: var(--ink);
    line-height: 1;
  }
</style>
</head>
<body>
<div class="canvas">
  <div class="cover">
    <svg class="doodles" viewBox="0 0 785 1120" aria-hidden="false">
      <g class="doodle-arrow" aria-hidden="true">
        <line x1="70" y1="57" x2="262" y2="57"/>
        <polyline points="252,50 263,57 252,64"/>
        <line x1="165" y1="1037" x2="280" y2="1037"/>
        <polyline points="270,1030 281,1037 270,1044"/>
      </g>
      <circle class="doodle" cx="364" cy="78" r="30" role="img" aria-label="Kritzelei Erdbeere"/>
      <circle class="doodle" cx="423" cy="130" r="32" role="img" aria-label="Kritzelei Cupcake"/>
      <circle class="doodle" cx="547" cy="76" r="28" role="img" aria-label="Kritzelei Krone"/>
      <circle class="doodle" cx="692" cy="84" r="34" role="img" aria-label="Kritzelei Sprechblase"/>
      <circle class="doodle" cx="136" cy="147" r="36" role="img" aria-label="Kritzelei Buch"/>
      <circle class="doodle" cx="263" cy="139" r="26" role="img" aria-label="Kritzelei Vogel"/>
      <circle class="doodle" cx="506" cy="157" r="20" role="img" aria-label="Kritzelei Blätterzweig"/>
      <circle class="doodle" cx="698" cy="152" r="20" role="img" aria-label="Kritzelei Zweig"/>
      <circle class="doodle" cx="111" cy="221" r="32" role="img" aria-label="Kritzelei Flügel"/>
      <circle class="doodle" cx="395" cy="221" r="32" role="img" aria-label="Kritzelei Kussgesicht"/>
      <circle class="doodle" cx="604" cy="221" r="34" role="img" aria-label="Kritzelei Lippen"/>
      <circle class="doodle" cx="736" cy="196" r="18" role="img" aria-label="Kritzelei Diamant"/>
      <circle class="doodle" cx="726" cy="300" r="30" role="img" aria-label="Kritzelei Flügel"/>
      <circle class="doodle" cx="118" cy="470" r="22" role="img" aria-label="Kritzelei Sprechblase"/>
      <circle class="doodle" cx="96" cy="543" r="26" role="img" aria-label="Kritzelei Handy"/>
      <circle class="doodle" cx="345" cy="495" r="18" role="img" aria-label="Kritzelei Zweig"/>
      <circle class="doodle" cx="730" cy="482" r="22" role="img" aria-label="Kritzelei Zweig"/>
      <circle class="doodle" cx="118" cy="845" r="34" role="img" aria-label="Kritzelei Hasenohren"/>
      <circle class="doodle" cx="244" cy="800" r="18" role="img" aria-label="Kritzelei Zweig"/>
      <circle class="doodle" cx="372" cy="792" r="28" role="img" aria-label="Kritzelei Lippen"/>
      <circle class="doodle" cx="534" cy="778" r="26" role="img" aria-label="Kritzelei Diamant"/>
      <circle class="doodle" cx="688" cy="770" r="34" role="img" aria-label="Kritzelei Pfeil und Bogen"/>
      <rect class="doodle" x="300" y="862" width="150" height="28" rx="14" role="img" aria-label="Kritzelei Banner mit Herzen"/>
      <circle class="doodle" cx="376" cy="918" r="18" role="img" aria-label="Kritzelei Blume"/>
      <circle class="doodle" cx="585" cy="900" r="26" role="img" aria-label="Kritzelei Lippenstift"/>
      <circle class="doodle" cx="686" cy="930" r="28" role="img" aria-label="Kritzelei Briefumschlag"/>
      <circle class="doodle" cx="92" cy="1040" r="34" role="img" aria-label="Kritzelei Vase mit Herzblumen"/>
    </svg>

    <h1 class="title">
      <span class="title__script title__script--first">Kritzeleien</span>
      <span class="title__link">AUS ZIMMER</span>
      <span class="title__script title__script--last">Neun</span>
    </h1>

    <p class="author">AUTHOR NAME</p>
  </div>
</div>
</body>
</html>
```